Poem Handwritten by Veteran while in the jungle of Vietnam

My parents are celebrating their 50th wedding anniversary this year. I wanted to give them a very memorable gift. On my parents 2nd anniversary, my father was stationed in Vietnam. On that night he was in the jungle waiting till morning and wrote a poem to my mother using his pant leg as paper. I would like this poem to typographically designed to be framed and hung on the wall.

I have attached a picture of the poem below. It will need to be 11x14 when printed for framing. It would be great if there was background or artwork to make it more visually interesting, perhaps in a watercolor. My parents have a transitional style. I have attached some possible color schemes as well. Cool greens, blue, neutral grays, with hints of berries or highlights of yellow. These are just a guide, I would be open to your interpretations.

Thank you for your help. This will hopefully be a gift they will truly treasure as much as the poem itself.

Target Market(s)

My parents who are excited to be celebrating their 50th wedding anniversary. It should have a transitional, mature style.

Font styles to use
Serif
Script

Requirements
Must have
• The poem, typographically designed. There can be a mix of fonts, but legibility is critically important.
• Now that some designs have come through I wanted to give some more guidance of what I'm looking for. I want something that feels sophisticated and artistic.
Nice to have
• A background or art work, using the color schemes attached as a guide. I am really liking the designs that have a full color landscape artwork in the background. The fonts should be elegant and formal. I really like the romantic, muted colors. I had trouble finding similar projects online in the style I wanted until I cam across wedding invites. Those seem to be the most applicable. I've added pictures of some so you can get a sense of what I'm looking for. I am really liking the jungle foliage, starry skies or sunrises.
Should not have
• Cartoon caricatures, fonts that are too illegible when printed. I'm not liking anything whimsical. I don't like the very bright colors for this project.

```html
<!DOCTYPE html>
<html lang="en">
<head>
<meta charset="utf-8">
<title>Happy Anniversary Darling – Anniversary Poem Print</title>
<link href="https://fonts.googleapis.com/css2?family=Pinyon+Script&family=Sorts+Mill+Goudy:ital@0;1&display=swap" rel="stylesheet">
<style>
  :root {
    --backdrop: #5a5a5a;
    --wine: #4a0120;
    --berry: #8c1a4b;
    --cream: #ffffff;
    --panel: rgba(255, 252, 248, 0.74);
    --rose-light: #eedcae;
    --rose-mid: #d9bd7e;
    --rose-deep: #a9793d;
    --rose-shadow: #6b4522;
  }
  * { box-sizing: border-box; margin: 0; padding: 0; }
  html, body {
    width: 1200px; height: 1200px; overflow: hidden;
    background: var(--backdrop);
  }
  .print {
    position: absolute; left: 225px; top: 102px;
    width: 786px; height: 1000px;
    overflow: hidden;
    box-shadow: 0 8px 22px rgba(0,0,0,0.45);
  }
  .rose-backdrop {
    position: absolute; inset: 0;
    background:
      radial-gradient(circle at 20% 40%, var(--rose-light) 0 14%, transparent 30%),
      radial-gradient(circle at 85% 55%, var(--rose-light) 0 12%, transparent 28%),
      radial-gradient(circle at 60% 95%, var(--rose-mid) 0 10%, transparent 26%),
      linear-gradient(180deg, var(--rose-deep) 0%, var(--rose-mid) 8%, var(--rose-light) 40%, var(--rose-mid) 75%, var(--rose-light) 100%);
  }
  .rose-strip {
    position: absolute; left: 0; top: 0; width: 100%; height: 63px;
    background: linear-gradient(90deg, var(--rose-shadow) 0%, var(--rose-deep) 25%, #c79a52 55%, #e2c063 75%, var(--rose-deep) 100%);
  }
  .title-band {
    position: absolute; left: 0; top: 63px; width: 100%; height: 226px;
    background: var(--wine);
  }
  .title {
    position: absolute; left: 0; width: 100%;
    font-family: "Pinyon Script", cursive;
    color: var(--cream);
    font-weight: 400;
    line-height: 1;
  }
  .title-line1 { top: 20px; left: 76px; width: auto; font-size: 92px; }
  .title-line2 { top: 100px; left: 278px; width: auto; font-size: 92px; }

  .poem-panel {
    position: absolute; left: 104px; top: 289px;
    width: 578px; height: 646px;
    background: var(--panel);
  }
  .poem-frame {
    position: absolute; left: 17px; top: 59px;
    width: 542px; height: 567px;
    border: 2px solid var(--berry);
    border-top: none;
  }
  .frame-top {
    position: absolute; top: 59px; height: 2px; background: var(--berry);
  }
  .frame-top.left { left: 17px; width: 107px; }
  .frame-top.right { left: 452px; width: 107px; }
  .flourish {
    position: absolute; top: 30px; width: 60px; height: 60px;
    background: radial-gradient(circle, rgba(140,26,75,0.55) 0 20%, rgba(140,26,75,0.15) 45%, transparent 70%);
  }
  .flourish.left { left: 118px; }
  .flourish.right { left: 400px; }
  .poem-heading {
    position: absolute; left: 170px; top: 44px; width: 240px;
    text-align: center;
    font-family: "Sorts Mill Goudy", serif;
    color: var(--berry);
    font-size: 11.5px; line-height: 16px;
  }
  .poem-column {
    position: absolute; top: 120px; width: 290px;
    text-align: center;
    font-family: "Sorts Mill Goudy", serif;
    font-style: italic;
    color: var(--berry);
    font-size: 14px; line-height: 18px;
  }
  .poem-column.left { left: 17px; }
  .poem-column.right { left: 285px; }
  .stanza { margin-bottom: 18px; }
</style>
</head>
<body>
  <main class="print">
    <div class="rose-backdrop" role="img" aria-label="Soft photograph of cream and golden roses filling the background"></div>
    <div class="rose-strip" role="img" aria-label="Close-up photograph of amber and yellow roses"></div>

    <header class="title-band">
      <h1 class="title title-line1">Happy Anniversary</h1>
      <div class="title title-line2">Darling</div>
    </header>

    <section class="poem-panel">
      <div class="poem-frame"></div>
      <div class="frame-top left"></div>
      <div class="frame-top right"></div>
      <div class="flourish left" role="img" aria-label="Decorative scroll ornament"></div>
      <div class="flourish right" role="img" aria-label="Decorative scroll ornament"></div>

      <p class="poem-heading">20 July 1970, Monday, LZ Meridian<br>Walter’s Anniversary Poem</p>

      <div class="poem-column left">
        <p class="stanza">Life’s journey began with a challenge,<br>It was heralded far and near.<br>The road led forever,<br>Its completion was known to be dear.</p>
        <p class="stanza">From the garden of light it proceeded,<br>To the valley of shadows it led.<br>Thorns and thistles adorned it,<br>Past abyss and crevice is sped.</p>
        <p class="stanza">The brave surged forward with courage,<br>The wise undaunted pressed on.<br>The mighty held high their banner,<br>We all awaited the dawn.</p>
        <p class="stanza">Though the pitfalls and hazards were many,<br>The pathway was clear in view.<br>Straight and sure it glided,<br>Its course we knew to be true.</p>
        <p class="stanza">I knew you, Sweetheart, beforehand,<br>So precious and sweet were you,<br>Our moments of bliss were priceless,<br>Each day brought us joy anew.</p>
        <p class="stanza">The call to progression beckoned,<br>At last I would have my chance–</p>
      </div>

      <div class="poem-column right">
        <p class="stanza">To clasp you to me forever,<br>And seal our divine romance.</p>
        <p class="stanza">I eagerly started the journey,<br>Though with sorrow, I left you behind.<br>With courage and faith I continued,<br>For I knew, that you later I’d find.</p>
        <p class="stanza">I diligently search for you, Darling,<br>The roadway was both bleak and fair.<br>Though the years grew long in number,<br>I did not give up in despair.</p>
        <p class="stanza">At last in the distance I saw you,<br>So beautiful, lovely, and sweet!<br>Your attention I struggled to capture,<br>Your love I wrested to meet.</p>
        <p class="stanza">What rapture was mine in fulfilment,<br>As now together we stand.<br>To cherish and love each other,<br>While our plans and dreams expand.</p>
        <p class="stanza">I love you, Darling, forever,<br>My life you have made replete.<br>Our eternal mansion beckons,<br>Your love has made it complete.</p>
      </div>
    </section>
  </main>
</body>
</html>
```